Website design for an Online pastry shop

Website Name : www.lanternandplum.example

Description of the website and its target audience
We are a premium pastry company producing delicious cakes, macarons, cookies, gelato, and other sweet dessert. Our differentiation is that our products are freshly produced with premium quality imported ingredients and one bite into our products set us apart from other bakery shop. We online retail online so as to provide high quality products at a affordable cost. Our products has received raving reviews by many food enthusiast even the hard to please ones. The products contain more natural ingredients and we do not add preservatives. The return rates for our pastry is almost 80%. You only need to try once to be return customers. Our greatest challenge is getting customer to take the first bite. We are so sure of our products that we are going to give people free food tasting.

We are based in China but all our products are developed by award winning chefs from 5 stars hotel. The target customer is woman 16 to 40+ in china. Working class ladies and demand high quality products. A modern, sophisticated and minimalist website

This is a competitive market and image is crucial for such a food ‘conscious ’ orientated customer. They want to feel that they are buying from a reliable company that take great effort to ensure food cleaniness and safety yet affordable price. We make almost 98% of sub ingredients ourselves and we make it by hand.

Style/theme ideas for the web page design
I am looking for a elegant a little rustic, handmade feel yet sophisticated design - one that is easy to the eye yet functional and easy for the user to navigate through. Good play of fonts to give let it feel unique and customised. Black and white is our corporate colours. However, we do not want black background as it does not tease the taste bud. All our colours should come from our products. Customers should be very close to our products. They eat with their eyes first. Black and white is just accent.

Inspirational and competitors websites
http://www.47tart.example/ ( Key competitor )
I like the simple, clean look. The products are the key focus
https://www.pelvora.example/
clean, fresh and different. Attractive with purpose. Feminine
http://moatandwillow.example/
this has a great layout - lots of information and nicely presented. Very sweet and feminine
http://www.storeharbourly.example/
product features is the focus
http://www.janetobrill.example/store/
fun, feminine, rustic

Number of pages needed : 6 ( Uncoded PSD design only )
Page descriptions
Home Page - This page will show what makes our products stand out from the competitors and provide an introduction of who we are.
2nd page : Product catalogue
3nd page: Detail Product page with pictures and descriptions. Select products size and add to cart....
4rd page: Brand Story with pictures and descriptions.
5th page Contact Us : Here they can contact or schedule an appointment for free product tasting
6th page : Check out page

• Please see the project wire frame file " main page.png " or file number 70

```html
<!DOCTYPE html>
<html lang="en">
<head>
<meta charset="utf-8">
<title>Lantern &amp; Plum — Home</title>
<link rel="stylesheet" href="https://fonts.googleapis.com/css2?family=Nunito+Sans:wght@400;600;700&display=swap">
<style>
:root{
  --orange:#f0913a;
  --charcoal:#555355;
  --ink:#444244;
  --line:#c9c9c9;
  --white:#ffffff;
  --muted:#777;
}
*{box-sizing:border-box;margin:0;padding:0}
html,body{width:694px;height:1200px;overflow:hidden;background:var(--white)}
body{font-family:"Nunito Sans",sans-serif;color:var(--ink);position:relative}
.abs{position:absolute}

/* header */
.promo{left:21px;top:12px;font-size:11px;color:var(--ink)}
.promo strong{color:var(--orange);font-weight:600}
.brand{left:247px;top:14px;width:200px;text-align:center}
.brand-dot{width:28px;height:28px;border-radius:50%;background:var(--charcoal);margin:0 auto 10px}
.brand-name{font-size:13px;font-weight:700;color:var(--charcoal);letter-spacing:.3px}
.btn-outline{border:1px solid var(--orange);color:var(--orange);font-size:10px;height:17px;line-height:15px;text-align:center;font-weight:600}
.login{left:566px;top:16px;width:49px}
.signup{left:623px;top:16px;width:50px}
.cart{left:593px;top:43px;width:57px;height:19px;background:var(--orange);color:var(--white);font-size:10px;line-height:19px;text-align:center}
.cart-icon{left:652px;top:43px;width:20px;height:19px;background:var(--orange);display:flex;align-items:center;justify-content:center}

.nav{left:0;top:90px;width:694px;height:25px;background:var(--charcoal);display:flex;justify-content:center;gap:27px;align-items:center}
.nav a{color:var(--white);font-size:11px;text-decoration:none}

/* hero */
.hero{left:0;top:118px;width:694px;height:272px;background:linear-gradient(100deg,#a9744a 0%,#e9e6e3 25%,#f2efec 50%,#b98a62 75%,#7b5640 100%)}
.hero-caption{left:443px;top:291px;width:251px;height:77px;background:rgba(85,83,85,.72);color:var(--white);text-align:right;padding:12px 21px 0 10px}
.hero-caption h2{font-size:13.5px;font-weight:600;letter-spacing:.2px;margin-bottom:6px}
.hero-caption p{font-size:9.5px;line-height:13px}

/* tagline */
.tag-rule{left:70px;top:437px;width:554px;height:1px;background:#999}
.tagline{left:159px;top:410px;width:376px;height:54px;border:1px solid #999;background:var(--white);text-align:center;font-size:8.5px;line-height:12px;padding-top:14px}
.divider{left:0;width:694px;height:1px;background:#e2e2e2}

/* featured */
.section-title{left:0;width:694px;text-align:center;font-size:16px;font-weight:600;color:var(--ink);letter-spacing:.3px}
.tile{top:560px;width:154px;height:155px}
.t1{left:21px;background:linear-gradient(160deg,#f0ece8 0%,#9e2030 45%,#efd9a8 80%,#f3efe9 100%)}
.t2{left:187px;background:linear-gradient(150deg,#3f3128,#5a4638 50%,#3a2d25)}
.t3{left:353px;background:radial-gradient(circle at 55% 40%,#b9814a,#6b4d35 70%,#4a3729)}
.t4{left:519px;background:linear-gradient(160deg,#f1ece8 0%,#e79a4a 50%,#8e2f3c 75%,#efe3d2 100%)}
.tile-label{left:44px;top:65px;width:66px;height:25px;border:1px solid rgba(255,255,255,.9);color:var(--white);font-size:13px;line-height:23px;text-align:center}
.tile-rule{top:77px;width:22px;height:1px;background:rgba(255,255,255,.9)}

/* newsletter */
.email-input{left:216px;top:821px;width:262px;height:18px;border:1px solid #888;border-radius:2px;font-size:8px;color:#aaa;padding-left:9px;line-height:16px}
.join{left:311px;top:851px;width:71px;height:24px;background:var(--orange);color:var(--white);font-size:12px;font-weight:600;line-height:24px;text-align:center}
.social{top:915px;width:24px;height:24px;border:1.3px solid var(--ink);border-radius:50%}

/* footer */
.footer{left:0;top:983px;width:694px;height:217px;background:var(--charcoal);color:var(--white)}
.footer .f-dot{left:337px;top:14px;width:20px;height:20px;border-radius:50%;background:var(--white)}
.footer .f-name{left:0;top:47px;width:694px;text-align:center;font-size:9.5px;letter-spacing:.8px;font-weight:600}
.f-link{font-size:9.5px;font-weight:600}
.f-menu{font-size:8.5px}
.f-contact{left:21px;font-size:9px}
.f-contact b{font-size:12px;font-weight:400}
.f-frame{left:542px;top:76px;width:131px;height:129px;border:1px solid #aaa;padding:3px}
.f-frame div{width:100%;height:100%;background:linear-gradient(150deg,#3f3128,#5a4638 50%,#3a2d25)}
</style>
</head>
<body>

<header>
  <p class="abs promo"><strong>Free Delivery</strong> for Orders above $50</p>
  <div class="abs brand"><div class="brand-dot"></div><div class="brand-name">Lantern &amp; Plum</div></div>
  <div class="abs btn-outline login">Login</div>
  <div class="abs btn-outline signup">Sign Up</div>
  <div class="abs cart">CART</div>
  <div class="abs cart-icon">
    <svg width="13" height="12" viewBox="0 0 13 12" fill="none" stroke="#fff" stroke-width="1.1"><path d="M0.5 1h2l1.6 6.5h6.5l1.4-5H3.2"/><circle cx="5" cy="10" r="1"/><circle cx="9.5" cy="10" r="1"/></svg>
  </div>
  <nav class="abs nav">
    <a href="#">Cakes</a><a href="#">Macarons</a><a href="#">Cookies</a><a href="#">Galeto</a><a href="#">Tasting Room</a><a href="#">About Us</a>
  </nav>
</header>

<section>
  <div class="abs hero" role="img" aria-label="Photo of a whipped-cream tart on a wooden board with a bread basket and teacup behind"></div>
  <div class="abs hero-caption">
    <h2>THIS IS A TRANSLUCENT BOX</h2>
    <p>Product Name on the Banner and a very short intro of the product below the banner.</p>
  </div>
</section>

<section>
  <div class="abs tag-rule"></div>
  <div class="abs tagline">We value flavor over fuss.<br>Artican, Handcrated and other gourmet confections delivered direct to your door.</div>
  <div class="abs divider" style="top:485px"></div>
</section>

<section>
  <h2 class="abs section-title" style="top:524px">FEATURED</h2>
  <div class="abs tile t1" role="img" aria-label="Photo of a cherry-topped cheesecake"></div>
  <div class="abs tile t2" role="img" aria-label="Photo of colourful macarons on a dark wooden table"></div>
  <div class="abs tile t3" role="img" aria-label="Blurred photo of cookies">
    <div class="abs tile-rule" style="left:22px"></div>
    <div class="abs tile-label">Cookies</div>
    <div class="abs tile-rule" style="left:110px"></div>
  </div>
  <div class="abs tile t4" role="img" aria-label="Photo of meringue pastries with fruit sorbet"></div>
  <div class="abs divider" style="top:744px"></div>
</section>

<section>
  <h2 class="abs section-title" style="top:784px">JOIN OUR EMAIL LIST BOX</h2>
  <div class="abs email-input">E-mail</div>
  <div class="abs join">JOIN</div>
  <div class="abs divider" style="top:897px;left:250px;width:193px;background:#d5d5d5"></div>
  <div class="abs social" style="left:285px"></div>
  <div class="abs social" style="left:318px"></div>
  <div class="abs social" style="left:351px"></div>
  <div class="abs social" style="left:383px"></div>
</section>

<footer class="abs footer">
  <div class="abs f-dot"></div>
  <div class="abs f-name">Lantern &amp; Plum</div>
  <span class="abs f-link" style="left:21px;top:74px">Costumer Service</span>
  <span class="abs f-link" style="left:121px;top:74px">About US</span>
  <span class="abs f-link" style="left:21px;top:104px">Questions ?</span>
  <p class="abs f-contact" style="top:178px">Phone Number: <b>4444444444</b></p>
  <p class="abs f-contact" style="top:192px">E-mail: <b>hello@lanternandplum.example</b></p>
  <span class="abs f-menu" style="left:466px;top:75px">Cakes</span>
  <span class="abs f-menu" style="left:466px;top:115px;text-decoration:underline">Macarons</span>
  <div class="abs" style="left:511px;top:121px;width:31px;height:1px;background:#ccc"></div>
  <span class="abs f-menu" style="left:466px;top:156px">Cookies</span>
  <span class="abs f-menu" style="left:466px;top:196px">Galeto</span>
  <div class="abs f-frame"><div role="img" aria-label="Photo of colourful macarons on a dark wooden table"></div></div>
</footer>

</body>
</html>
```